Thank You For Shopping / Hair Care Tips

I need “Thank You For Shopping”
Post cards made for my hair business !
I added pictures of post cards that I really like . I also added my LuzeKora Wigs logo for you guys to use

I want the backside of the flyer to have hair care tips !
I want people to have full directions on how to care for their wigs

Target Market(s)

Im marking to young woman to older middle aged woman
Ages 23-66 . I want my flyer to look mature And classy

Industry/Entity Type

Hair And Beauty

Font styles to use
Serif
Script

Colors
e34699
e34298
e34398

Requirements
Must have
• The flyer must have the Instagram logo with my Instagram name next to it @luze.kora.wigs__
• Also it must have my “Luze Kora Wigs” logo that I’ve uploaded in the pictures section .
• Flyer had to be two sides . One side “ thank you for shopping “ side two “hair care tips”
• My website must be on the flyer - www.luzekorawigs.example
• The flyer must match the colors of my logo
• All white . With the pink and glitter sliver you see on my logo
Nice to have
• Nice to have a glitter border
Should not have
• The flyer should not have different colors that don’t match my logo
• It shouldn’t be made without having my Instagram or website on the flyer

```html
<!DOCTYPE html>
<html lang="en">
<head>
<meta charset="utf-8">
<title>Luze Kora Wigs – Thank You Postcard</title>
<link rel="stylesheet" href="https://fonts.googleapis.com/css2?family=Great+Vibes&family=Playfair+Display:wght@700&family=Montserrat:wght@700;800&family=Open+Sans:wght@400;600&display=swap">
<style>
  :root {
    --pink: #e34699;
    --pink-deep: #e34298;
    --ink: #3a3a3c;
    --ink-soft: #555558;
    --silver-1: #d9d9dc;
    --silver-2: #9c9ca1;
    --silver-3: #f4f4f6;
    --white: #ffffff;
    --backdrop: #e6e6e9;
  }
  * { box-sizing: border-box; margin: 0; padding: 0; }
  html, body { width: 1200px; height: 800px; overflow: hidden; }
  body {
    background: var(--backdrop);
    position: relative;
    font-family: "Open Sans", sans-serif;
  }
  .postcard {
    position: absolute;
    top: 200px;
    width: 560px;
    height: 400px;
    overflow: hidden;
    background:
      radial-gradient(circle at 22% 30%, rgba(255,255,255,.95) 0 6%, transparent 7%),
      radial-gradient(circle at 70% 18%, rgba(255,255,255,.9) 0 5%, transparent 6%),
      radial-gradient(circle at 82% 62%, rgba(255,255,255,.85) 0 7%, transparent 8%),
      radial-gradient(circle at 40% 72%, rgba(255,255,255,.85) 0 5%, transparent 6%),
      linear-gradient(135deg, #f7f7f9 0%, #dfdfe3 50%, #f3f3f5 100%);
    box-shadow: 0 6px 18px rgba(0,0,0,.18);
  }
  .postcard--front { left: 30px; }
  .postcard--back { left: 610px; }

  .glitter-rule {
    position: absolute;
    left: 0; right: 0;
    height: 6px;
    background: repeating-linear-gradient(90deg, var(--silver-2) 0 3px, var(--silver-3) 3px 5px, var(--silver-1) 5px 8px);
  }
  .pink-band {
    position: absolute;
    left: 0; right: 0;
    background: var(--pink);
    color: var(--white);
    display: flex;
    align-items: center;
  }

  /* Front */
  .thank-you {
    position: absolute;
    top: 8px; left: 30px;
    font-family: "Great Vibes", cursive;
    font-size: 118px;
    line-height: 1;
    color: var(--ink);
  }
  .front-rule-top { top: 132px; }
  .headline-band {
    top: 138px; height: 62px;
    justify-content: center;
    font-family: "Playfair Display", serif;
    font-size: 40px;
    letter-spacing: 1px;
  }
  .front-rule-bottom { top: 200px; }
  .brand-name {
    position: absolute;
    top: 240px; left: 32px;
    width: 230px;
    font-family: "Playfair Display", serif;
    font-size: 34px;
    line-height: 1.05;
    color: var(--pink);
  }
  .connect {
    position: absolute;
    top: 226px; left: 300px;
  }
  .connect-title {
    font-family: "Montserrat", sans-serif;
    font-weight: 800;
    font-size: 17px;
    color: var(--pink);
    border-bottom: 1px solid var(--ink-soft);
    padding-bottom: 4px;
    margin-bottom: 6px;
  }
  .handle {
    display: flex;
    align-items: center;
    gap: 8px;
    font-family: "Playfair Display", serif;
    font-size: 17px;
    color: var(--ink-soft);
    line-height: 1.45;
  }
  .handle-mark {
    width: 13px; height: 13px;
    background: var(--silver-2);
    flex: none;
  }
  .shop-band {
    bottom: 0; height: 44px;
    padding: 0 20px;
    gap: 16px;
    font-family: "Montserrat", sans-serif;
    font-weight: 700;
    font-size: 13px;
  }
  .shop-band .site { font-size: 15px; }
  .front-rule-shop { bottom: 44px; }
  .gem {
    position: absolute;
    width: 56px; height: 42px;
    border-radius: 6px;
    background: radial-gradient(circle at 40% 40%, #ffffff 0%, #d4d4d8 55%, #a5a5ab 100%);
  }
  .gem--front { right: 12px; bottom: 26px; }

  /* Back */
  .tips-title {
    position: absolute;
    top: 10px; left: 34px;
    font-family: "Great Vibes", cursive;
    font-size: 64px;
    line-height: 1;
    color: var(--ink);
  }
  .tips {
    position: absolute;
    top: 90px; left: 30px; right: 26px;
    font-size: 10px;
    line-height: 1.42;
    color: var(--ink);
  }
  .tips ul { list-style: none; }
  .tips li::before {
    content: "•";
    color: var(--pink);
    margin-right: 5px;
  }
  .tips-subhead {
    font-family: "Montserrat", sans-serif;
    font-weight: 800;
    font-size: 12px;
    color: var(--pink);
    margin: 6px 0 2px;
  }
  .back-rule { bottom: 50px; }
  .tag-band {
    bottom: 0; height: 50px;
    justify-content: flex-end;
    padding-right: 26px;
    gap: 10px;
    font-family: "Montserrat", sans-serif;
    font-weight: 800;
    font-size: 15px;
  }
  .tag-band .handle-mark { background: var(--white); width: 14px; height: 14px; }
  .gem--back { left: 22px; bottom: 20px; width: 70px; height: 48px; }
</style>
</head>
<body>

  <section class="postcard postcard--front">
    <h1 class="thank-you">Thank You</h1>
    <div class="glitter-rule front-rule-top"></div>
    <div class="pink-band headline-band">FOR YOUR SHOPPING</div>
    <div class="glitter-rule front-rule-bottom"></div>

    <div class="brand-name">Luze Kora Wigs</div>

    <div class="connect">
      <div class="connect-title">STAY CONNECTED</div>
      <div class="handle"><span class="handle-mark"></span>@LUZE.KORA.WIGS</div>
      <div class="handle"><span class="handle-mark"></span>@LUZE.KORA.WIGS</div>
      <div class="handle"><span class="handle-mark"></span>@LUZEKORA</div>
    </div>

    <div class="glitter-rule front-rule-shop"></div>
    <div class="pink-band shop-band">
      <span>SHOP ONLINE BY VISITING US AT</span>
      <span class="site">WWW.LUZEKORAWIGS.EXAMPLE</span>
    </div>
    <div class="gem gem--front" role="img" aria-label="Sparkling diamond gemstone"></div>
  </section>

  <section class="postcard postcard--back">
    <h2 class="tips-title">Hair Care Tips</h2>
    <div class="tips">
      <ul>
        <li>Apply a moisture rich Conditioner and comb hair, starting with the ends working your way to your scalp.</li>
        <li>Leave Conditioner in for at least 15 minutes or more.</li>
        <li>Do not massage the hair.</li>
        <li>Rinse thoroughly.</li>
        <li>Scrunch hair gently to enhance the curls. (For wavy/curly patterns)</li>
        <li>When damp, apply a dime size of an anti-frizz alcohol free hair serum.</li>
        <li>Let air-dry.</li>
        <li>Do not use oil products or excessive products on curly hair, it will cause matting.</li>
        <li>Do not brush or comb hair when dry. It will cause hair to frizz and may cause hair to tangle.</li>
      </ul>
      <div class="tips-subhead">BED TIME CARE</div>
      <ul>
        <li>Before going to bed, braid your hair into one loose large braid and wear a satin scarf or bonnet.</li>
        <li>After waking up, undo braid and comb using a wide tooth comb or paddle brush, beginning at the ends and working your way to roots.</li>
        <li>Style as needed.</li>
      </ul>
    </div>
    <div class="glitter-rule back-rule"></div>
    <div class="pink-band tag-band">
      <span>TAG US ON INSTAGRAM</span>
      <span class="handle-mark"></span>
      <span>@LUZE.KORA.WIGS</span>
    </div>
    <div class="gem gem--back" role="img" aria-label="Pair of sparkling diamond gemstones"></div>
  </section>

</body>
</html>
```